New Brava Tiles Billboard at HQ

Looking to design a catchy image / theme for a billboard located just above our corporate HQ showroom and warehouse, along the service road of a 6-lane highway. Billboard measures 8ft x 24 ft. Would like to highlight that the store location is directly beneath the sign.

We are a retail and wholesale business selling premium flooring, ready to assemble cabinets, and granite countertops. See image ideas attached. Our information:
NAME: Brava Tiles, Cabinets, Countertops
ADDRESS: 412 W. Hwy 29, Duncanville, TX 75990
WEBSITE: www.bravatiles-example.com
PHONE: 555-8-DECKED (555-833-2533)

```html
<!DOCTYPE html>
<html lang="en">
<head>
<meta charset="utf-8">
<title>Brava Tiles Billboard</title>
<link rel="stylesheet" href="https://fonts.googleapis.com/css2?family=Montserrat:wght@500;600;700;800&display=swap">
<style>
  :root {
    --green: #7dc733;
    --green-dark: #5e9e22;
    --black: #141414;
    --white: #ffffff;
    --ink: #1b1b1b;
    --wood-light: #b88a5e;
    --wood-mid: #9c6d45;
    --wood-dark: #7a5234;
    --backdrop: #d6d6d6;
  }
  * { margin: 0; padding: 0; box-sizing: border-box; }
  html, body { width: 1200px; height: 1091px; overflow: hidden; }
  body {
    background: var(--backdrop);
    font-family: "Montserrat", sans-serif;
    position: relative;
  }
  .billboard {
    position: absolute;
    left: 40px; top: 359px;
    width: 1120px; height: 373px;
    overflow: hidden;
    box-shadow: 0 10px 24px rgba(0,0,0,0.35);
    background: linear-gradient(180deg, var(--wood-mid) 0%, var(--wood-light) 35%, var(--wood-mid) 65%, var(--wood-dark) 100%);
  }
  .billboard__shapes { position: absolute; inset: 0; }
  .brand {
    position: absolute; left: 52px; top: 30px;
    display: flex; align-items: center; gap: 12px;
  }
  .brand__mark { width: 26px; height: 26px; background: var(--green); }
  .brand__name { font-size: 38px; font-weight: 800; color: var(--ink); letter-spacing: -0.5px; white-space: nowrap; }
  .nav {
    position: absolute; left: 392px; top: 20px;
    display: flex; align-items: center; white-space: nowrap;
    color: var(--white); font-weight: 700; font-size: 21px; letter-spacing: 0.3px;
  }
  .nav__sep { width: 2px; height: 24px; background: var(--green); margin: 0 12px; }
  .tagline {
    position: absolute; left: 150px; width: 660px; top: 163px;
    text-align: center; color: var(--white);
    font-size: 25px; font-weight: 600; line-height: 35px;
    -webkit-text-stroke: 0.6px #2a1a0d;
    text-shadow: 0 0 3px #2a1a0d, 1px 1px 2px #2a1a0d;
  }
  .contact {
    position: absolute; left: 128px; top: 295px;
    width: 700px; height: 44px; display: flex;
    border-radius: 22px; overflow: hidden;
  }
  .contact__web {
    background: var(--black); color: var(--white);
    width: 330px; display: flex; align-items: center; gap: 8px;
    padding-left: 10px; font-size: 16px; font-weight: 500; white-space: nowrap;
    border-radius: 0 22px 22px 0; position: relative; z-index: 1;
  }
  .contact__web b { color: var(--green); font-weight: 700; }
  .contact__phone {
    background: var(--green); color: var(--black);
    flex: 1; margin-left: -22px; padding-left: 30px;
    display: flex; align-items: center; gap: 10px;
    font-size: 19px; font-weight: 800; white-space: nowrap;
  }
  .icon-circle {
    width: 26px; height: 26px; border-radius: 50%;
    background: var(--white); display: flex; align-items: center; justify-content: center;
    flex-shrink: 0;
  }
  .locator {
    position: absolute; left: 853px; top: 30px; width: 247px;
    text-align: center;
  }
  .locator__title {
    margin-top: 24px; color: var(--green);
    font-size: 44px; font-weight: 800; line-height: 1.05;
  }
  .locator__divider {
    margin: 10px auto 0; width: 205px;
    display: flex; align-items: center; gap: 6px;
  }
  .locator__divider span { flex: 1; height: 1px; background: var(--ink); }
  .locator__address {
    margin-top: 8px; color: var(--ink);
    font-size: 25px; font-weight: 800; line-height: 1.28;
  }
</style>
</head>
<body>
  <section class="billboard" aria-label="Brava Tiles billboard">
    <svg class="billboard__shapes" width="1120" height="373" viewBox="0 0 1120 373">
      <defs>
        <linearGradient id="propsTone" x1="0" y1="0" x2="1" y2="1">
          <stop offset="0" stop-color="#c9c9c4"/>
          <stop offset="0.4" stop-color="#4a4a40"/>
          <stop offset="1" stop-color="#1e1f22"/>
        </linearGradient>
      </defs>
      <rect x="0" y="113" width="170" height="260" fill="url(#propsTone)" opacity="0.85" role="img" aria-label="Photo of binoculars, a map, a magnifying glass and a notebook on the floor"/>
      <polygon points="350,0 1120,0 1120,63 305,63" fill="var(--black)"/>
      <polygon points="352,0 374,0 329,63 307,63" fill="var(--green)"/>
      <polygon points="0,0 345,0 265,113 0,113" fill="var(--white)"/>
      <rect x="815" y="30" width="60" height="34" rx="17" fill="var(--green)"/>
      <path d="M853,50 Q853,30 873,30 L1080,30 Q1100,30 1100,50 L1100,292 L976,362 L853,292 Z" fill="var(--white)"/>
      <polyline points="868,283 976,326 1084,283" fill="none" stroke="var(--green)" stroke-width="12"/>
    </svg>

    <div class="brand">
      <span class="brand__mark"></span>
      <span class="brand__name">Brava Tiles</span>
    </div>

    <nav class="nav">
      <span>FLOOR</span><span class="nav__sep"></span>
      <span>CABINETS</span><span class="nav__sep"></span>
      <span>COUNTERTOPS</span>
    </nav>

    <p class="tagline">We are a retail and wholesale business selling premium flooring, ready to assemble cabinets, and granite countertops.</p>

    <div class="contact">
      <div class="contact__web">
        <span class="icon-circle">
          <svg width="18" height="18" viewBox="0 0 18 18" fill="none" stroke="#141414" stroke-width="1.3">
            <circle cx="9" cy="9" r="7.5"/><ellipse cx="9" cy="9" rx="3.3" ry="7.5"/>
            <line x1="1.5" y1="9" x2="16.5" y2="9"/><line x1="2.8" y1="5" x2="15.2" y2="5"/><line x1="2.8" y1="13" x2="15.2" y2="13"/>
          </svg>
        </span>
        <span>www.<b>bravatiles-example</b>.com</span>
      </div>
      <div class="contact__phone">
        <span class="icon-circle">
          <svg width="16" height="16" viewBox="0 0 24 24" fill="#7dc733">
            <path d="M6.6 10.8a15.1 15.1 0 0 0 6.6 6.6l2.2-2.2a1 1 0 0 1 1-.25 11.4 11.4 0 0 0 3.6.57 1 1 0 0 1 1 1V20a1 1 0 0 1-1 1A17 17 0 0 1 3 4a1 1 0 0 1 1-1h3.5a1 1 0 0 1 1 1c0 1.25.2 2.45.57 3.570a1 1 0 0 1-.25 1z"/>
          </svg>
        </span>
        <span>555-8-DECKED (555-833-2533)</span>
      </div>
    </div>

    <div class="locator">
      <h2 class="locator__title">WE ARE<br>HERE</h2>
      <div class="locator__divider">
        <span></span>
        <svg width="16" height="22" viewBox="0 0 16 22">
          <path d="M8 0C3.6 0 0 3.5 0 7.9 0 13.8 8 22 8 22s8-8.2 8-14.1C16 3.5 12.4 0 8 0z" fill="#e8303a"/>
          <circle cx="8" cy="8" r="3" fill="#fff"/>
        </svg>
        <span></span>
      </div>
      <p class="locator__address">412 W. Hwy 29,<br>Duncanville,<br>TX 75990</p>
    </div>
  </section>
</body>
</html>
```